Business Cards for Retail/Sourcing Business.

We need a business cards for our company where it looks like:
TK
LV

VERTICAL, where the TK is over the LV. Then Under the TKLV would be name, address and website address. We want the P to be in the style of our original logo, which I uploaded.

Also, can we get a couple of designs with fun colors - especially for the letter head.

Target Market(s)

Old clients. Many of our clients or people we do business with are 40-50 plus. We are not an industry with many young people.

Industry/Entity Type

Business

Contact Information for Business Card

Front side is just says TKLV with name, title, address, and website below.

Font styles to use
Serif
Sans Serif
Decorative
Script

Requirements
Must have
• THE TKLV design with the P in the design of the logo
Nice to have
• Fun colors, new takes on the TKLV and any other additions that would be cool and make it pop

```html
<!DOCTYPE html>
<html lang="en">
<head>
<meta charset="utf-8">
<title>TKLV Business Card</title>
<link rel="stylesheet" href="https://fonts.googleapis.com/css2?family=Exo+2:ital,wght@1,600&family=Montserrat:wght@500;600;700&family=Roboto+Condensed:wght@400&display=swap">
<style>
  :root {
    --backdrop: #e4dfdf;
    --card-white: #ffffff;
    --band-black: #000000;
    --accent-red: #ee1c25;
    --ink: #1a1a1a;
  }
  html, body {
    margin: 0;
    width: 1200px;
    height: 1000px;
    overflow: hidden;
    background: var(--backdrop);
  }
  .business-card {
    position: absolute;
    left: 476px;
    top: 245px;
    width: 279px;
    height: 463px;
    background: var(--card-white);
  }
  .brand-band {
    height: 232px;
    background: var(--band-black);
    display: flex;
    flex-direction: column;
    align-items: center;
    justify-content: center;
  }
  .brand-name {
    margin: 0;
    color: var(--card-white);
    font-family: "Montserrat", sans-serif;
    font-weight: 700;
    font-size: 74px;
    line-height: 72px;
    letter-spacing: 2px;
    text-align: center;
  }
  .brand-name span { display: block; }
  .holder {
    text-align: center;
    margin-top: 36px;
  }
  .holder-name {
    margin: 0;
    color: var(--accent-red);
    font-family: "Exo 2", sans-serif;
    font-style: italic;
    font-weight: 600;
    font-size: 18px;
    letter-spacing: 1px;
    line-height: 20px;
  }
  .holder-title {
    margin: 0;
    color: var(--ink);
    font-family: "Roboto Condensed", sans-serif;
    font-size: 13px;
    line-height: 16px;
  }
  .contact {
    position: absolute;
    left: 52px;
    top: 376px;
    font-family: "Montserrat", sans-serif;
    font-size: 12.5px;
  }
  .contact-web {
    display: flex;
    align-items: center;
    gap: 5px;
    color: var(--ink);
    font-weight: 600;
    margin: 0 0 8px 0;
  }
  .contact-address {
    margin: 0;
    color: var(--accent-red);
    font-weight: 500;
    line-height: 14px;
    font-style: normal;
  }
</style>
</head>
<body>
  <div class="business-card">
    <header class="brand-band">
      <h1 class="brand-name"><span>TK</span><span>LV</span></h1>
    </header>
    <section class="holder">
      <p class="holder-name">MARLO QUENBY</p>
      <p class="holder-title">Home Sourcing</p>
    </section>
    <section class="contact">
      <p class="contact-web">
        <svg class="icon-globe" width="11" height="11" viewBox="0 0 12 12" aria-hidden="true">
          <g fill="none" stroke="var(--accent-red)" stroke-width="1.1">
            <circle cx="6" cy="6" r="5"/>
            <ellipse cx="6" cy="6" rx="2.2" ry="5"/>
            <line x1="1" y1="6" x2="11" y2="6"/>
          </g>
        </svg>
        www.tklvsourcing.com
      </p>
      <address class="contact-address">000 Harbour Vale Street<br>Area Name, NSW, 0000</address>
    </section>
  </div>
</body>
</html>
```